luxury contemporary fashion website needs simple, elegant flowchart to describe the buying and selli

* Luxury, resale, preloved items are sold on this online platform
*Horizontal, simple, flowchart with 5 steps in 'friendly' font with a simple emoticon/ picture for each step
*To be positioned in the 'How we work' tab of the webpage to explain in a very simple manner the buying and selling process for the customers.
*Attached is a very rudimentary mock-up of what we would like included and an idea of a project similar to what we desire
* to confirm the text for each step, we have also attached a word file below

Industry/Entity Type

Fashion

Font styles to use
Sans Serif

Colors
86cfc6
cfeae6

Requirements
Must have
• Simple drawing / shape after each point In the closest to 'duck egg blue' fill colour you can find with a black outline

```html
<!DOCTYPE html>
<html lang="en">
<head>
<meta charset="utf-8">
<title>Bespoke Concierge Service – How We Work</title>
<link href="https://fonts.googleapis.com/css2?family=Oswald:wght@400;500;600&display=swap" rel="stylesheet">
<style>
  :root {
    --page: #ffffff;
    --duck-egg: #86cfc6;
    --duck-egg-light: #b9e3dd;
    --ink: #2e3433;
    --ink-soft: #5b6a68;
    --badge: #2d2f2f;
    --disc: #c8202f;
    --white: #ffffff;
    --tone-box: #f07a2a;
    --tone-hand: #e9b64a;
    --tone-parcel: #f2c230;
    --tone-cart: #8a8f96;
    --tone-cash: #3f9b6a;
  }
  * { box-sizing: border-box; margin: 0; padding: 0; }
  html, body { width: 1200px; height: 750px; overflow: hidden; background: var(--page); }
  body { font-family: "Oswald", "Arial Narrow", sans-serif; position: relative; }

  .panel {
    position: absolute; left: 10px; top: 23px; width: 1177px; height: 665px;
    background: var(--duck-egg); border-radius: 4px;
  }
  .title-rule {
    position: absolute; top: 91px; height: 3px; width: 240px;
    background: linear-gradient(90deg, transparent, var(--duck-egg-light) 25%, var(--duck-egg-light) 75%, transparent);
  }
  .title-rule.left { left: 44px; }
  .title-rule.right { left: 890px; }
  .title {
    position: absolute; top: 58px; left: 0; width: 1200px; text-align: center;
    font-weight: 500; font-size: 50px; line-height: 66px; letter-spacing: 0.5px; color: var(--ink);
  }

  .step {
    position: absolute; top: 188px; width: 240px;
    display: flex; flex-direction: column; align-items: center; text-align: center;
  }
  .step-heading {
    height: 64px; display: flex; align-items: flex-end; justify-content: center;
    font-weight: 500; font-size: 25px; line-height: 28px; color: var(--ink);
  }
  .step-icon { margin-top: 12px; width: 116px; height: 116px; display: block; }
  .step-number {
    margin-top: 14px; width: 28px; height: 28px; border-radius: 50%;
    background: var(--badge); color: var(--white);
    font-size: 17px; font-weight: 500; line-height: 28px;
  }
  .step-text {
    margin-top: 24px; font-weight: 500; font-size: 19px; line-height: 23px; color: var(--ink-soft);
  }
  .accent { display: inline-block; vertical-align: middle; margin-left: 4px; }
  .currency {
    position: absolute; font-size: 22px; color: var(--white); font-weight: 400;
  }
</style>
</head>
<body>
  <div class="panel"></div>
  <div class="title-rule left"></div>
  <div class="title-rule right"></div>
  <h1 class="title">BESPOKE CONCIERGE SERVICE</h1>

  <section class="step" style="left:44px">
    <h2 class="step-heading">HAVE ITEMS<br>TO SELL?</h2>
    <svg class="step-icon" viewBox="0 0 116 116" role="img" aria-label="Hands holding a parcel">
      <circle cx="58" cy="58" r="58" fill="var(--disc)"/>
      <rect x="26" y="34" width="64" height="50" rx="4" fill="var(--tone-box)"/>
    </svg>
    <div class="step-number">1</div>
    <p class="step-text">BRAND SPANKING<br>OR NEARLY NEW<svg class="accent" width="18" height="14" viewBox="0 0 18 14" aria-hidden="true"><circle cx="4" cy="9" r="2" fill="var(--white)"/><circle cx="13" cy="9" r="2" fill="var(--white)"/><circle cx="9" cy="3" r="2" fill="var(--white)"/></svg></p>
  </section>

  <section class="step" style="left:249px">
    <h2 class="step-heading">PERSONAL<br>COLLECTION</h2>
    <svg class="step-icon" viewBox="0 0 116 116" role="img" aria-label="Hand picking up stacked items">
      <circle cx="58" cy="58" r="58" fill="var(--disc)"/>
      <rect x="30" y="28" width="56" height="60" rx="8" fill="var(--tone-hand)"/>
    </svg>
    <div class="step-number">2</div>
    <p class="step-text">WE CHOOSE<br>THE PIECES<br>WE KNOW<br>THE VELORA<br>CUSTOMERS WILL<br>LOVE<svg class="accent" width="18" height="16" viewBox="0 0 24 22" aria-hidden="true"><path d="M12 21 L2.5 11.5 A5.5 5.5 0 0 1 12 4 A5.5 5.5 0 0 1 21.5 11.5 Z" fill="var(--white)"/></svg></p>
  </section>

  <section class="step" style="left:482px">
    <h2 class="step-heading">WE PREPARE</h2>
    <svg class="step-icon" viewBox="0 0 116 116" role="img" aria-label="Sealed cardboard package">
      <circle cx="58" cy="58" r="58" fill="var(--disc)"/>
      <rect x="32" y="32" width="52" height="52" rx="4" fill="var(--tone-parcel)"/>
    </svg>
    <div class="step-number">3</div>
    <p class="step-text">YOUR ITEM<br>FOR SALE<br>WITH THOROUGH<br>AUTHENTICITY &amp;<br>CONDITION CHECKS<br>FROM THE VELORA<br>TEAM …<br>SO YOU DON'T<br>HAVE TO!<svg class="accent" width="18" height="18" viewBox="0 0 18 18" aria-hidden="true"><circle cx="9" cy="9" r="7.5" fill="none" stroke="var(--white)" stroke-width="1.5"/></svg></p>
  </section>

  <section class="step" style="left:697px">
    <h2 class="step-heading">ONCE SOLD</h2>
    <svg class="step-icon" viewBox="0 0 116 116" role="img" aria-label="Shopping cart">
      <circle cx="58" cy="58" r="58" fill="var(--disc)"/>
      <path d="M22 30 H34 L42 74 H86" fill="none" stroke="var(--tone-cart)" stroke-width="4" stroke-linecap="round" stroke-linejoin="round"/>
      <path d="M36 38 H92 L86 64 H40 Z" fill="var(--white)" stroke="var(--tone-cart)" stroke-width="3" stroke-linejoin="round"/>
      <circle cx="48" cy="86" r="6" fill="#2b3a4a"/>
      <circle cx="80" cy="86" r="6" fill="#2b3a4a"/>
    </svg>
    <div class="step-number">4</div>
    <p class="step-text">WE LOVINGLY<br>PREPARE<br>THE ITEM<br>SHIPPED VIA<br>TRACKED<br>SERVICES</p>
    <svg width="48" height="40" viewBox="0 0 48 40" style="position:absolute;left:165px;top:550px" aria-hidden="true">
      <path d="M4 22 L44 14 Q48 14 44 18 L8 26 Z M20 19 L30 4 L35 4 L30 17 Z M22 24 L28 38 L33 38 L32 22 Z M6 23 L2 14 L6 14 L11 21 Z" fill="#d6efeb"/>
    </svg>
  </section>

  <section class="step" style="left:912px">
    <h2 class="step-heading">YOUR<br>PAYMENT</h2>
    <svg class="step-icon" viewBox="0 0 116 116" role="img" aria-label="Bundle of banknotes">
      <circle cx="58" cy="58" r="58" fill="var(--disc)"/>
      <rect x="24" y="36" width="68" height="44" rx="3" fill="var(--tone-cash)"/>
    </svg>
    <div class="step-number">5</div>
    <p class="step-text">I) POCKET<br>THE CASH<br>II) DONATE TO<br>CHARITY<br>FULL OR<br>PARTIAL AMOUNT<svg class="accent" width="22" height="24" viewBox="0 0 22 24" aria-hidden="true"><ellipse cx="11" cy="3" rx="6" ry="2" fill="none" stroke="var(--white)" stroke-width="1.3"/><circle cx="11" cy="14" r="8" fill="none" stroke="var(--white)" stroke-width="1.5"/></svg></p>
    <span class="currency" style="left:145px;top:400px">€</span>
    <span class="currency" style="left:165px;top:390px">£</span>
    <span class="currency" style="left:166px;top:420px">$</span>
  </section>
</body>
</html>
```